Disability Service Provider Website

We are working with VEP, which provides services and job training designed to educate, facilitate, train, and assist individuals with disabilities. They describe their clients using words like Unity and Unique.
Some sites to use for content/competitors and inspiration:
https://www.skillmora.com
https://www.pwkd.org
https://www.bellowhaven.org
https://www.openmeadow.org
https://corvelan.org
Thank you for taking the time to consider designing a website for us. We are web developers based in Stockton, CA, USA. Most of our projects go through the same process. Understanding this process may help you win a project with us. We custom-code all of our websites in-house. We don’t have any requirements as to what tools you use for your design, but we prefer Figma files. For any design that we label as four-stars, we send it to the client for review. The client picks the final design they want us to use. Once we complete this process, we will continue to show additional clients all the four-star sites and purchase them later. Your designs will have multiple chances to sell. For better chances of success, we ask that you follow these guidelines.
IMAGES:
If you use any images or icons in the design, we ask that you have a link to the asset so we can purchase the image/icon. Most of the designs we submit do not have the customer’s images on them unless they have some great images. Be creative; show us the feeling you are trying to portray with your image choices. Use any royalty-free site you choose. We subscribe to Stellic and mainly use their images, but we can purchase images outside of Stellic.
PLEASE NOTE: we will not submit designs to clients with watermarks on the images.
FONTS:
We ask that you identify the fonts used in the design. This can be done in a message if you want. We typically use Bramble Fonts and Stellic Fonts.
CONTENT:
We're always open to different content and ideas. We often submit designs with stock images so the client can see our vision. We typically take pictures after the website launch to use their images with our vision. Lorem Ipsum is fine for paragraphs, but we ask that you write the headers in correct English. We want to be able to show the vision and identify the sections of the website.
INSPIRATION:
We typically add a couple of links in the brief of websites we like to help you get started in your design.
REVISIONS:
We do not often ask for revisions of the designs unless we see something in the design that may not appeal to the client. If there are slight changes that we want to make, we do that in the development process.
FEEDBACK:
We rarely give feedback on designs during the design process. We are working on many website projects and do not have the time to provide feedback. We usually respond if your request is well thought out and asks specific questions, but a note asking “feedback, please” usually goes unanswered.
Number of Pages Required
1 page
Look and feel
Each slider illustrates characteristics of the customer's brand and the style your logo design should communicate.

```html
<!DOCTYPE html>
<html lang="en">
<head>
<meta charset="utf-8">
<title>VEP – Celebrating Unity and Uniqueness</title>
<link href="https://fonts.googleapis.com/css2?family=Ubuntu:wght@400;500;700&family=Open+Sans:wght@400;600;700&display=swap" rel="stylesheet">
<style>
:root{
  --red:#8c0f16;
  --red-deep:#6e0d12;
  --ink:#2b2b2b;
  --text:#4a4a4a;
  --band:#f2f2f2;
  --charcoal:#2e2e2e;
  --white:#ffffff;
}
*{margin:0;padding:0;box-sizing:border-box}
html,body{width:1200px;height:3445px;overflow:hidden;background:var(--white)}
body{position:relative;font-family:"Open Sans",sans-serif;color:var(--text)}
.abs{position:absolute}
a{color:inherit;text-decoration:none}

/* top bar */
.topbar{position:absolute;top:0;left:530px;width:670px;height:40px}
.topbar svg{position:absolute;top:0;left:0}
.topbar .mail{position:absolute;left:202px;top:11px;color:var(--white);font:600 15px "Open Sans",sans-serif}
.topbar .call{position:absolute;left:417px;top:11px;color:var(--white);font:600 15px "Open Sans",sans-serif}
.brand{position:absolute;left:112px;top:14px;font:700 56px/1 "Ubuntu",sans-serif;color:var(--red);letter-spacing:-1px}
.nav{position:absolute;top:70px;left:0;width:1200px;height:20px;font:400 14px "Open Sans",sans-serif;color:var(--ink)}
.nav a{position:absolute;top:0}
.nav a.active{font-weight:600}

/* hero */
.hero{position:absolute;top:114px;left:0;width:1200px;height:428px;overflow:hidden}
.hero-photo{position:absolute;left:0;top:0;width:800px;height:428px;background:linear-gradient(110deg,#6b4a36 0%,#b98b5f 28%,#e7c24a 48%,#d9d3c8 70%,#efefef 100%)}
.hero svg{position:absolute;left:0;top:0}
.hero .kicker{position:absolute;left:729px;top:70px;color:var(--white);font:400 24px "Open Sans",sans-serif}
.hero h1{position:absolute;left:729px;top:108px;color:var(--white);font:700 45px/48px "Ubuntu",sans-serif}
.hero p{position:absolute;left:729px;top:222px;color:var(--white);font:400 15.5px/28px "Open Sans",sans-serif}
.btn-ghost{position:absolute;left:736px;top:307px;width:227px;height:42px;border:2px solid var(--white);border-radius:21px;color:var(--white);font:700 14.5px/38px "Open Sans",sans-serif;text-align:center}

/* common sections */
.section-title{position:absolute;font:500 44px/1.1 "Ubuntu",sans-serif;color:var(--ink)}
.section-title em{font-style:normal;color:var(--red)}
.copy{position:absolute;font:400 15px/28px "Open Sans",sans-serif;color:var(--text)}
.copy p+p{margin-top:8px}
.btn{position:absolute;width:144px;height:42px;border-radius:21px;background:var(--red);color:var(--white);font:700 14.5px/42px "Open Sans",sans-serif;text-align:center}
.photo-circle{position:absolute;border-radius:50%}
.frame{position:absolute;border:3px solid var(--red)}

/* services */
.services{position:absolute;top:1109px;left:0;width:1200px;height:474px;background:var(--band)}
.service{position:absolute;top:156px;width:240px;text-align:center}
.service .icon{width:112px;height:112px;margin:0 auto;border-radius:50%;background:var(--white);box-shadow:0 3px 10px rgba(0,0,0,.08);display:flex;align-items:center;justify-content:center}
.service h3{margin-top:20px;font:500 18px "Ubuntu",sans-serif;color:var(--ink)}
.service p{margin-top:12px;font:400 14px/28px "Open Sans",sans-serif;color:var(--text)}
.arrow{position:absolute;top:1393px;width:34px;height:34px}

/* impact */
.impact{position:absolute;top:2653px;left:0;width:1200px;height:475px;background:var(--band)}
.impact .lead{position:absolute;top:132px;left:0;width:1200px;text-align:center;font:400 15px/28px "Open Sans",sans-serif}
.stat{position:absolute;width:164px;height:164px;border-radius:50%;background:radial-gradient(circle at 50% 45%,#ffffff 55%,#f3eaea 78%,#e6d3d4 100%);box-shadow:0 4px 10px rgba(0,0,0,.06);text-align:center}
.stat.grey{background:radial-gradient(circle at 50% 45%,#ffffff 55%,#ececec 78%,#dcdcdc 100%)}
.stat strong{display:block;margin-top:50px;font:500 42px/1 "Ubuntu",sans-serif;color:var(--red)}
.stat.grey strong{color:var(--ink)}
.stat span{display:block;margin-top:10px;font:400 17px "Open Sans",sans-serif;color:var(--text)}

/* footer */
.footer{position:absolute;top:3128px;left:0;width:1200px;height:317px;background:linear-gradient(100deg,#2a2a2a 0%,#2f2b2b 40%,#6a1318 75%,#8c0f16 100%);color:var(--white)}
.footer .brand-foot{position:absolute;left:118px;top:52px;font:700 96px/1 "Ubuntu",sans-serif;color:var(--white)}
.footer h4{position:absolute;top:56px;font:500 16px "Ubuntu",sans-serif;letter-spacing:.3px}
.footer ul{position:absolute;top:96px;list-style:none;font:400 14.5px/26px "Open Sans",sans-serif}
.footer .contact{position:absolute;left:452px;top:96px;font:400 14.5px/26px "Open Sans",sans-serif}
.footer .contact div{position:relative;padding-left:30px}
.footer .contact svg{position:absolute;left:0;top:6px}
.footer .legal{position:absolute;top:275px;left:0;width:1200px;text-align:center;font:400 14px "Open Sans",sans-serif}
</style>
</head>
<body>

<header>
  <div class="topbar">
    <svg width="670" height="40" viewBox="0 0 670 40">
      <polygon points="0,0 165,0 165,40 0,40 14,20" fill="#e6e6e6"/>
      <polygon points="165,0 385,0 400,20 385,40 165,40 180,20" fill="var(--red)"/>
      <polygon points="385,0 670,0 670,40 385,40 400,20" fill="var(--charcoal)"/>
      <circle cx="50" cy="20" r="10" fill="#1e1e1e"/>
      <circle cx="89" cy="20" r="10" fill="#1e1e1e"/>
      <circle cx="129" cy="20" r="10" fill="#1e1e1e"/>
    </svg>
    <span class="mail">Mail Us: info@vep.org</span>
    <span class="call">Call: +1-555-014-2290</span>
  </div>
  <div class="brand">VEP</div>
  <nav class="nav">
    <a class="active" style="left:421px">HOME</a>
    <a style="left:496px">ABOUT</a>
    <a style="left:575px">WHAT WE DO</a>
    <a style="left:699px">REAL STORIES</a>
    <a style="left:825px">BLOG</a>
    <a style="left:891px">GET INVOLVED</a>
    <a style="left:1022px">CONTACT</a>
  </nav>
</header>

<section class="hero">
  <div class="hero-photo" role="img" aria-label="Photo of a smiling child in a wheelchair being pushed by a cheerful adult at home"></div>
  <svg width="1200" height="428" viewBox="0 0 1200 428">
    <defs>
      <linearGradient id="heroRed" x1="0" y1="0" x2="1" y2="0">
        <stop offset="0" stop-color="#8c0f16"/>
        <stop offset="0.55" stop-color="#5e1418"/>
        <stop offset="1" stop-color="#2e2b2b"/>
      </linearGradient>
    </defs>
    <path d="M730 0 H1200 V428 H790 C690 428 600 350 600 220 C600 100 660 0 730 0 Z" fill="#d8d8d8" opacity="0.85"/>
    <path d="M780 0 H1200 V428 H820 C710 428 634 335 634 215 C634 95 700 0 780 0 Z" fill="url(#heroRed)"/>
  </svg>
  <div class="kicker">Welcome to VEP</div>
  <h1>Celebrating Unity<br>and Uniqueness.</h1>
  <p>Empowering individuals with disabilities through<br>education, training, and support</p>
  <a class="btn-ghost">GIVE HELP THAT WORKS</a>
</section>

<section class="mission">
  <h2 class="section-title" style="left:111px;top:662px">Our <em>Mission</em></h2>
  <div class="copy" style="left:112px;top:725px">
    <p>Lorem ipsum dolor sit amet, consectetur adipisjdcing elit, sed do<br>eiusmod tempor incididunt ut labore et dolornkne magna aliqua.<br>Quis ipsum suspendisse ultrices gravida. Risus commodo viverra<br>maecenas accumsan lacus vel facilisis.</p>
    <p>Lorem ipsum dolor sit amet, consectetur adipisjdcing elit, sed do<br>eiusmod tempor incididunt ut labore et dolornkne magna aliqua.<br>Quis ipsum suspendisse ultrices gravida.</p>
  </div>
  <a class="btn" style="left:112px;top:953px">LEARN MORE</a>
  <div class="frame" style="left:670px;top:776px;width:226px;height:236px"></div>
  <div class="photo-circle" style="left:707px;top:616px;width:382px;height:382px;background:radial-gradient(circle at 45% 40%,#c9a48c,#7d5a48 60%,#3b3535)" role="img" aria-label="Photo of a woman giving a high five to a young boy in a wheelchair"></div>
</section>

<section class="services">
  <h2 class="section-title" style="left:0;top:64px;width:1200px;text-align:center">What <em>We Do</em></h2>
  <div class="service" style="left:102px">
    <div class="icon"><svg width="54" height="54" viewBox="0 0 54 54" fill="none" stroke="#333" stroke-width="1.6"><path d="M5 20 h18 a4 4 0 0 1 4 4 v24 a4 4 0 0 0-4-4 H5z M49 20 H31 a4 4 0 0 0-4 4 v24 a4 4 0 0 1 4-4 h18z"/><circle cx="27" cy="10" r="6" stroke="var(--red)"/><path d="M10 28h10M10 34h10M34 28h10M34 34h10"/></svg></div>
    <h3>Skillmora Grow</h3>
    <p>Lorem ipsum dolor sit ametcor<br>adipiscing elit, sed do eiusmod<br>tempor incididunt ut labore.</p>
  </div>
  <div class="service" style="left:356px">
    <div class="icon"><svg width="58" height="54" viewBox="0 0 58 54" fill="none" stroke="#333" stroke-width="1.6"><rect x="22" y="8" width="32" height="24"/><circle cx="12" cy="20" r="5" stroke="var(--red)"/><path d="M4 46 v-12 a8 8 0 0 1 16 0 v12 M20 30 l10-6"/><path d="M32 26v-6M38 26v-10M44 26v-8M50 26v-12" stroke="var(--red)"/></svg></div>
    <h3>Onsite Training</h3>
    <p>Lorem ipsum dolor sit ametcor<br>adipiscing elit, sed do eiusmod<br>tempor incididunt ut labore.</p>
  </div>
  <div class="service" style="left:610px">
    <div class="icon"><svg width="54" height="54" viewBox="0 0 54 54" fill="none" stroke="#333" stroke-width="1.6"><path d="M5 30 h18 a4 4 0 0 1 4 4 v14 a4 4 0 0 0-4-4 H5z M49 30 H31 a4 4 0 0 0-4 4 v14 a4 4 0 0 1 4-4 h18z"/><circle cx="27" cy="15" r="9" stroke="var(--red)"/><path d="M23 15l3 3 5-6" stroke="var(--red)"/></svg></div>
    <h3>Training Conductor</h3>
    <p>Lorem ipsum dolor sit ametcor<br>adipiscing elit, sed do eiusmod<br>tempor incididunt ut labore.</p>
  </div>
  <div class="service" style="left:865px">
    <div class="icon"><svg width="60" height="54" viewBox="0 0 60 54" fill="none" stroke="#333" stroke-width="1.6"><rect x="26" y="6" width="30" height="22"/><path d="M37 12l8 5-8 5z" stroke="var(--red)"/><rect x="4" y="24" width="26" height="18"/><path d="M2 46h30"/><circle cx="17" cy="31" r="3" stroke="var(--red)"/></svg></div>
    <h3>Custom eLearning</h3>
    <p>Lorem ipsum dolor sit ametcor<br>adipiscing elit, sed do eiusmod<br>tempor incididunt ut labore.</p>
  </div>
</section>
<svg class="arrow" style="left:42px" viewBox="0 0 34 34"><circle cx="17" cy="17" r="16" fill="none" stroke="#999" stroke-width="1.4"/><path d="M19.5 11l-6 6 6 6" fill="none" stroke="#999" stroke-width="1.6"/></svg>
<svg class="arrow" style="left:1122px" viewBox="0 0 34 34"><circle cx="17" cy="17" r="16" fill="none" stroke="#222" stroke-width="1.4"/><path d="M14.5 11l6 6-6 6" fill="none" stroke="#222" stroke-width="1.6"/></svg>

<section class="help">
  <div class="frame" style="left:306px;top:1810px;width:226px;height:234px"></div>
  <div class="photo-circle" style="left:111px;top:1649px;width:382px;height:382px;background:radial-gradient(circle at 55% 50%,#f0c23a,#c98a1e 55%,#7a5a2a)" role="img" aria-label="Photo of a happy girl with glasses in a yellow raincoat outdoors"></div>
  <h2 class="section-title" style="left:623px;top:1695px">How to <em>Help</em></h2>
  <div class="copy" style="left:624px;top:1757px">
    <p>Lorem ipsum dolor sit amet, consectetur adipisjdcing elit, sed do<br>eiusmod tempor incididunt ut labore et dolornkne magna aliqua.<br>Quis ipsum suspendisse ultrices gravida. Risus commodo viverra<br>maecenas accumsan lacus vel facilisis.</p>
    <p>Lorem ipsum dolor sit amet, consectetur adipisjdcing elit, sed do<br>eiusmod tempor incididunt ut labore et dolornkne magna aliqua.<br>Quis ipsum suspendisse ultrices gravida.</p>
  </div>
  <a class="btn" style="left:624px;top:1986px">LEARN MORE</a>
</section>

<section class="events">
  <h2 class="section-title" style="left:111px;top:2194px;line-height:51px">Upcoming Events<br><em>and Trainings</em></h2>
  <div class="copy" style="left:112px;top:2315px">
    <p>Quis ipsum suspendisse ultrices gravida. Risus commodo viverra<br>maecenas accumsan lacus vel facilisis.</p>
    <p>Lorem ipsum dolor sit amet, consectetur adipisjdcing elit, sed do<br>eiusmod tempor incididunt ut labore et dolornkne magna aliqua.<br>Quis ipsum suspendisse ultrices gravida.</p>
  </div>
  <a class="btn" style="left:112px;top:2484px">LEARN MORE</a>
  <div class="frame" style="left:670px;top:2308px;width:226px;height:234px"></div>
  <div class="photo-circle" style="left:707px;top:2146px;width:382px;height:382px;background:radial-gradient(circle at 50% 45%,#f4f1ee,#d7d2cf 55%,#8c8c93)" role="img" aria-label="Photo of a smiling woman showing a tablet to a boy in a wheelchair"></div>
</section>

<section class="impact">
  <h2 class="section-title" style="left:0;top:61px;width:1200px;text-align:center">Our <em>Impact</em></h2>
  <p class="lead">Lorem ipsum dolor sit amet, consectetur adipiscing elit, sed do eiusmod tempor incididunt ut labore et dolore<br>magna aliqua. Quis ipsum suspendisse ultrices gravida. Risus commodo viverra maecenas accumsan.</p>
  <div class="stat" style="left:145px;top:223px"><strong>5,758</strong><span>Lorem Ipsum</span></div>
  <div class="stat grey" style="left:393px;top:257px"><strong>2,057</strong><span>Lorem Ipsum</span></div>
  <div class="stat" style="left:642px;top:223px"><strong>5,000</strong><span>Lorem Ipsum</span></div>
  <div class="stat grey" style="left:889px;top:257px"><strong>250</strong><span>Lorem Ipsum</span></div>
</section>

<footer class="footer">
  <div class="brand-foot">VEP</div>
  <svg class="abs" style="left:152px;top:192px" width="112" height="30" viewBox="0 0 112 30">
    <circle cx="15" cy="15" r="13" fill="var(--white)"/>
    <circle cx="57" cy="15" r="13" fill="var(--white)"/>
    <circle cx="97" cy="15" r="13" fill="var(--white)"/>
  </svg>
  <h4 style="left:452px">CONTACT US</h4>
  <div class="contact">
    <div><svg width="12" height="16" viewBox="0 0 12 16"><path d="M6 0a6 6 0 0 1 6 6c0 4-6 10-6 10S0 10 0 6a6 6 0 0 1 6-6z" fill="#fff"/><circle cx="6" cy="6" r="2.2" fill="#333"/></svg>VEP,<br>Address comes here.</div>
    <div style="margin-top:10px"><svg width="14" height="14" viewBox="0 0 14 14"><path d="M3 0l3 3-2 2c1 2 3 4 5 5l2-2 3 3-2 3C6 14 0 8 0 2z" fill="#fff"/></svg>+1-555-014-2290</div>
    <div style="margin-top:12px"><svg width="15" height="11" viewBox="0 0 15 11"><rect width="15" height="11" fill="#fff"/><path d="M0 0l7.5 6L15 0" fill="none" stroke="#333" stroke-width="1.2"/></svg>info@vep.org</div>
  </div>
  <h4 style="left:726px">QUICK LINKS</h4>
  <ul style="left:727px">
    <li>Campaign</li><li>About</li><li>What We Do</li><li>Real Stories</li><li>Ways To Give</li>
  </ul>
  <h4 style="left:947px">OTHER LINKS</h4>
  <ul style="left:949px">
    <li>Get Involved</li><li>Contact</li><li>Terms &amp; Conditions</li><li>Privacy Policy</li>
  </ul>
  <p class="legal">2024 VEP. All Rights Reserved.</p>
</footer>

</body>
</html>
```